Brantley Yard Services Flyer Design

I need a new flyer design for my business, Brantley Yard Services. I’ll be providing my old flyer and logo as references. The new flyer should feature updated wording, contact information, logos, and photos, but still keep the original “What We Do” section and include the phrase “Don’t See? Just Ask!” somewhere near the services. The flyer needs to look great in black and white for door-to-door handouts but also be eye-catching and professional enough for social media use.

The updated content should include the headline “Transforming Outdoor Spaces with Hard Work & Precision” and highlight three main service areas: Landscaping Services (project-based landscaping to clean, prepare, and transform outdoor spaces with precision), Property Cleanup (quick hauls, debris removal, or full cleanouts—no job too big or small), and Ground Preparation (pad preparation, brush removal, and fire lines—making properties safe, functional, and project-ready).

Please also include a “Why Choose Us?” section that lists: Locally owned since 2022, Reliable & affordable – no corners cut, Professional results you can trust, LICENSED AND Insured, and Quality work / on time / references / flexible / follow-up.

At the bottom, include the contact details: Call or Text Today!
www.brantleyyard.example
| sales@brantleyyard.example
| (555) 014-2793

The overall design should be clean, professional, and easy to read with a layout that clearly shows what we offer. Use visuals that represent outdoor services, landscaping, and property cleanup/prep work. I want something that feels trustworthy, family-friendly, and modern.
Use the same photo of leaf clean up from the original flyer if possible.
Our company colors are also black and white. For the most part.

```html
<!DOCTYPE html>
<html lang="en">
<head>
<meta charset="utf-8">
<title>Brantley Yard Services Flyer</title>
<link rel="stylesheet" href="https://fonts.googleapis.com/css2?family=Michroma&family=Orbitron:wght@400;800&family=Poppins:wght@400;600;700;800&family=Saira:ital,wght@1,800&display=swap">
<style>
:root{
  --ink:#0e0e10;
  --navy:#0d1220;
  --paper:#eeeeee;
  --column:#7a7a7a;
  --card:#7d7d7d;
  --white:#ffffff;
  --text:#1a1a1a;
}
*{margin:0;padding:0;box-sizing:border-box}
html,body{width:984px;height:1200px;overflow:hidden;background:var(--paper)}
.flyer{position:relative;width:984px;height:1200px;overflow:hidden;background:var(--paper);font-family:"Poppins",sans-serif;color:var(--text)}
.hero-photo{position:absolute;left:0;top:0;width:984px;height:362px;background:linear-gradient(135deg,#3a3a3a 0%,#262626 45%,#1c1c1c 100%)}
.backdrop{position:absolute;left:0;top:0}
.brand{position:absolute;left:60px;top:48px;display:flex;align-items:center;gap:12px;color:var(--white);font-family:"Poppins",sans-serif;font-weight:800;font-size:30px;line-height:1.05;width:340px}
.brand-mark{width:54px;height:54px;border-radius:50%;background:var(--white);flex:none}
.headline-lead{position:absolute;left:60px;top:160px;font-family:"Michroma",sans-serif;font-size:25px;line-height:32px;color:var(--white)}
.headline-main{position:absolute;left:58px;top:224px;font-family:"Saira",sans-serif;font-style:italic;font-weight:800;font-size:60px;line-height:55px;color:var(--white)}
.photo-column{position:absolute;left:582px;top:0;width:342px;height:902px;background:var(--column);border-radius:0 0 34px 34px}
.photo{position:absolute;left:28px;width:286px;height:246px;border:2px solid var(--white);border-radius:22px}
.photo.patio{top:55px;background:linear-gradient(160deg,#bdbdbd,#6d6d6d 60%,#8f8f8f)}
.photo.debris{top:340px;background:linear-gradient(160deg,#9a9a9a,#4a4a4a 55%,#7a7a7a)}
.photo.leaves{top:624px;background:linear-gradient(170deg,#a9a9a9,#7b7b7b 50%,#555)}
.section-title{position:absolute;font-family:"Orbitron",sans-serif;font-size:26px;color:var(--ink);letter-spacing:.5px}
.section-title .light{font-weight:400}
.section-title .bold{font-weight:800}
.areas-title{left:60px;top:390px}
.service{position:absolute;left:60px;width:450px}
.service-head{display:flex;align-items:center;gap:10px}
.service-icon{width:36px;height:36px;border-radius:50%;background:var(--navy);display:flex;align-items:center;justify-content:center}
.service-name{font-weight:700;font-size:17.5px;color:var(--ink)}
.service-desc{margin-top:10px;font-size:12.5px;line-height:15px}
.ask-bar{position:absolute;left:56px;top:711px;width:438px;height:57px;background:var(--card);border-radius:10px;display:flex;align-items:center}
.ask-dark{height:100%;width:227px;background:var(--ink);border-radius:10px;border:2px solid var(--white);display:flex;align-items:center;justify-content:center;color:var(--white);font-weight:800;font-size:27px}
.ask-light{flex:1;text-align:center;color:var(--white);font-weight:800;font-size:27px}
.do-title{left:60px;top:784px}
.card{position:absolute;top:840px;width:154px;height:234px;background:var(--card);border-radius:12px;overflow:hidden}
.card-head{height:47px;background:var(--ink);color:var(--white);font-weight:700;font-size:14px;line-height:15px;padding:0 12px;display:flex;align-items:center;border-bottom:2px solid var(--white)}
.card ul{list-style:none;padding:10px 10px 0 14px}
.card li{display:flex;gap:5px;color:var(--white);font-size:13.5px;line-height:16px;margin-bottom:12px}
.card li svg{flex:none;margin-top:3px}
.why-title{left:582px;top:917px;line-height:32px}
.why-text{position:absolute;left:582px;top:992px;width:320px;font-size:12.6px;line-height:16.7px;color:var(--ink)}
.cta{position:absolute;left:60px;top:1090px;font-weight:800;font-size:25px;color:var(--ink)}
.contacts{position:absolute;left:60px;top:1130px;display:flex;align-items:center;gap:10px;font-size:16px;color:var(--ink)}
.contact-icon{width:26px;height:26px;border-radius:50%;background:var(--navy);display:flex;align-items:center;justify-content:center}
.web{position:absolute;left:586px;top:1122px;font-size:25px;color:var(--white);letter-spacing:.3px}
</style>
</head>
<body>
<main class="flyer">
  <div class="hero-photo" role="img" aria-label="Darkened photo of a pile of hauled junk and carpet debris"></div>
  <svg class="backdrop" width="984" height="1200" viewBox="0 0 984 1200" aria-hidden="true">
    <polygon points="0,1083 640,1083 560,1166 0,1166" fill="var(--white)"/>
    <polygon points="508,1166 584,1096 984,1096 984,1200 0,1200 0,1166" fill="var(--navy)"/>
  </svg>

  <div class="brand"><span class="brand-mark"></span><span>Brantley Yard Services</span></div>
  <h1>
    <span class="headline-lead">Transforming Outdoor<br>Spaces with</span>
    <span class="headline-main">Hard Work &amp;<br>Precision</span>
  </h1>

  <div class="photo-column">
    <div class="photo patio" role="img" aria-label="Finished backyard with gravel area, retaining wall and wooden fence"></div>
    <div class="photo debris" role="img" aria-label="Pile of removed carpet, furniture and junk ready for hauling"></div>
    <div class="photo leaves" role="img" aria-label="Leaf clean up in a yard under a large weeping tree"></div>
  </div>

  <h2 class="section-title areas-title"><span class="light">OUR </span><span class="bold">SERVICE AREAS</span></h2>

  <section class="service" style="top:432px">
    <div class="service-head"><span class="service-icon"><svg width="18" height="18" viewBox="0 0 18 18"><path d="M9 3v8M9 7l-3-3M9 7l3-3M3 12h12l-2 3H5z" stroke="#fff" stroke-width="1.6" fill="none"/></svg></span><span class="service-name">LANDSCAPING SERVICES</span></div>
    <p class="service-desc">Project-based landscaping to clean, prepare, and transform<br>outdoor spaces with precision</p>
  </section>
  <section class="service" style="top:519px">
    <div class="service-head"><span class="service-icon"><svg width="18" height="18" viewBox="0 0 18 18"><path d="M2 9l7-6 7 6M4 8v8h10V8" stroke="#fff" stroke-width="1.6" fill="none"/></svg></span><span class="service-name">PROPERTY CLEANUP</span></div>
    <p class="service-desc">Quick hauls, debris removal, or full cleanouts—no job too<br>big or small</p>
  </section>
  <section class="service" style="top:606px">
    <div class="service-head"><span class="service-icon"><svg width="18" height="18" viewBox="0 0 18 18"><path d="M9 2v9M5 11h8l2 4H3z" stroke="#fff" stroke-width="1.6" fill="none"/></svg></span><span class="service-name">GROUND PREPARATION</span></div>
    <p class="service-desc">Pad preparation, brush removal, and fire lines—making<br>properties safe, functional, and project-ready.</p>
  </section>

  <div class="ask-bar"><span class="ask-dark">DON’T SEE?</span><span class="ask-light">JUST ASK!</span></div>

  <h2 class="section-title do-title"><span class="light">WHAT </span><span class="bold">WE DO</span></h2>

  <section class="card" style="left:60px">
    <div class="card-head">REMOVE</div>
    <ul>
      <li><svg width="11" height="11" viewBox="0 0 11 11"><circle cx="5.5" cy="5.5" r="4.6" stroke="#fff" fill="none"/><path d="M3.2 5.6l1.6 1.6 3-3.2" stroke="#fff" fill="none"/></svg>Junk removal</li>
      <li><svg width="11" height="11" viewBox="0 0 11 11"><circle cx="5.5" cy="5.5" r="4.6" stroke="#fff" fill="none"/><path d="M3.2 5.6l1.6 1.6 3-3.2" stroke="#fff" fill="none"/></svg>Trash &amp;<br>waste hauling</li>
      <li><svg width="11" height="11" viewBox="0 0 11 11"><circle cx="5.5" cy="5.5" r="4.6" stroke="#fff" fill="none"/><path d="M3.2 5.6l1.6 1.6 3-3.2" stroke="#fff" fill="none"/></svg>Yard &amp;<br>garden cleanup</li>
      <li><svg width="11" height="11" viewBox="0 0 11 11"><circle cx="5.5" cy="5.5" r="4.6" stroke="#fff" fill="none"/><path d="M3.2 5.6l1.6 1.6 3-3.2" stroke="#fff" fill="none"/></svg>Appliance<br>removal</li>
    </ul>
  </section>
  <section class="card" style="left:226px">
    <div class="card-head">INSTALL</div>
    <ul>
      <li><svg width="11" height="11" viewBox="0 0 11 11"><circle cx="5.5" cy="5.5" r="4.6" stroke="#fff" fill="none"/><path d="M3.2 5.6l1.6 1.6 3-3.2" stroke="#fff" fill="none"/></svg>Mulch</li>
      <li><svg width="11" height="11" viewBox="0 0 11 11"><circle cx="5.5" cy="5.5" r="4.6" stroke="#fff" fill="none"/><path d="M3.2 5.6l1.6 1.6 3-3.2" stroke="#fff" fill="none"/></svg>D.G.</li>
      <li><svg width="11" height="11" viewBox="0 0 11 11"><circle cx="5.5" cy="5.5" r="4.6" stroke="#fff" fill="none"/><path d="M3.2 5.6l1.6 1.6 3-3.2" stroke="#fff" fill="none"/></svg>Plants</li>
      <li><svg width="11" height="11" viewBox="0 0 11 11"><circle cx="5.5" cy="5.5" r="4.6" stroke="#fff" fill="none"/><path d="M3.2 5.6l1.6 1.6 3-3.2" stroke="#fff" fill="none"/></svg>Rock</li>
    </ul>
  </section>
  <section class="card" style="left:389px;width:153px">
    <div class="card-head">MAINTENANCE<br>&amp; OTHER</div>
    <ul>
      <li><svg width="11" height="11" viewBox="0 0 11 11"><circle cx="5.5" cy="5.5" r="4.6" stroke="#fff" fill="none"/><path d="M3.2 5.6l1.6 1.6 3-3.2" stroke="#fff" fill="none"/></svg>Yard clean up</li>
      <li><svg width="11" height="11" viewBox="0 0 11 11"><circle cx="5.5" cy="5.5" r="4.6" stroke="#fff" fill="none"/><path d="M3.2 5.6l1.6 1.6 3-3.2" stroke="#fff" fill="none"/></svg>Weed<br>prevention<br>(pre-emergent)</li>
      <li><svg width="11" height="11" viewBox="0 0 11 11"><circle cx="5.5" cy="5.5" r="4.6" stroke="#fff" fill="none"/><path d="M3.2 5.6l1.6 1.6 3-3.2" stroke="#fff" fill="none"/></svg>Roof &amp;<br>gutter cleaning</li>
      <li><svg width="11" height="11" viewBox="0 0 11 11"><circle cx="5.5" cy="5.5" r="4.6" stroke="#fff" fill="none"/><path d="M3.2 5.6l1.6 1.6 3-3.2" stroke="#fff" fill="none"/></svg>Fence &amp;<br>deck staining</li>
    </ul>
  </section>

  <h2 class="section-title why-title"><span class="light">WHY</span><br><span class="bold">CHOOSE US?</span></h2>
  <p class="why-text">Locally owned since 2022, Reliable &amp; affordable – no corners cut, Professional results you can trust, LICENSED AND Insured, and Quality work / on time / references / flexible / follow-up.</p>

  <p class="cta">CALL OR TEXT TODAY!</p>
  <div class="contacts">
    <span class="contact-icon"><svg width="14" height="14" viewBox="0 0 14 14"><path d="M3 1.5l2 .3.8 2.6-1.3 1a7 7 0 0 0 4 4l1-1.3 2.6.8.3 2a1.4 1.4 0 0 1-1.4 1.4A10.5 10.5 0 0 1 1.6 2.9 1.4 1.4 0 0 1 3 1.5z" fill="#fff"/></svg></span>
    <span>(555) 014-2793</span>
    <span class="contact-icon"><svg width="14" height="14" viewBox="0 0 14 14"><rect x="1.5" y="3" width="11" height="8" fill="none" stroke="#fff" stroke-width="1.3"/><path d="M1.5 3l5.5 4.5L12.5 3" fill="none" stroke="#fff" stroke-width="1.3"/></svg></span>
    <span>sales@brantleyyard.example</span>
  </div>
  <p class="web">www.brantleyyard.example</p>
</main>
</body>
</html>
```